distributor of aftermarket auto electrical components

I am after business card design for my new company called
Summit Vehicle Supplies (SVS as the acronym). I will supplying automotive wiring components, basically from battery to headlight. I will be aiming to sell in the 4wd scene and to auto electricians. i am not worried which colours are used though i would like it to be dynamic.
Updates

sorry guys, i have add a mobile and e-mail address that will need to on there as well. Sorry for theĀ inconvenience.

sorry guys i had erred on my spelling with my e-mail. i have now fixed it in the brief

Target Market(s)

4wd industry, custom cars, RV, auto electricians

Industry/Entity Type

Electrical

Requirements
Must have
• Company Name
ABN number: 71 306 548 290
Director: Derek Holloway
M 0432 718 946
E dhollo@fernwire.com.au

```html
<!DOCTYPE html>
<html lang="en">
<head>
<meta charset="utf-8">
<title>Summit Vehicle Supplies — Business Card</title>
<link rel="stylesheet" href="https://fonts.googleapis.com/css2?family=Arimo:wght@400;700&display=swap">
<style>
  :root {
    --page-bg: #e9e7e2;
    --card-bg: #f7f6f1;
    --brand-blue: #2f86d0;
    --brand-red: #e5393b;
    --text-blue: #2f80c8;
    --rule-red: #ef8a8a;
    --card-shadow: rgba(40, 30, 20, 0.18);
  }
  * { box-sizing: border-box; margin: 0; padding: 0; }
  html, body {
    width: 1200px;
    height: 900px;
    overflow: hidden;
    background: var(--page-bg);
    font-family: "Arimo", Arial, sans-serif;
  }
  .sheet {
    width: 1200px;
    height: 900px;
    display: flex;
    align-items: center;
    justify-content: center;
    gap: 60px;
  }
  .card {
    width: 520px;
    height: 316px;
    background: var(--card-bg);
    box-shadow: 0 6px 18px var(--card-shadow);
    position: relative;
  }

  /* Front */
  .card--front {
    display: flex;
    flex-direction: column;
    align-items: center;
    justify-content: center;
    gap: 22px;
  }
  .brand-mark {
    display: flex;
    align-items: center;
    gap: 18px;
  }
  .brand-mark__dot {
    width: 64px;
    height: 64px;
    border-radius: 50%;
    background: var(--brand-red);
  }
  .brand-mark__initials {
    font-weight: 700;
    font-size: 92px;
    line-height: 1;
    color: var(--brand-blue);
    letter-spacing: 2px;
  }
  .brand-name {
    font-weight: 700;
    font-size: 27px;
    color: var(--brand-blue);
  }

  /* Back */
  .card--back {
    display: flex;
    align-items: center;
    padding: 0 40px 0 48px;
  }
  .back-mark {
    display: flex;
    align-items: center;
    gap: 10px;
    width: 200px;
  }
  .back-mark__dot {
    width: 34px;
    height: 34px;
    border-radius: 50%;
    background: var(--brand-red);
  }
  .back-mark__initials {
    font-weight: 700;
    font-size: 50px;
    line-height: 1;
    color: var(--brand-blue);
  }
  .contact {
    border-left: 1px solid var(--rule-red);
    padding: 14px 0 14px 18px;
    margin-left: 20px;
  }
  .contact__name {
    font-weight: 700;
    font-size: 19px;
    color: var(--brand-red);
  }
  .contact__role {
    font-size: 11px;
    color: var(--text-blue);
    margin-bottom: 8px;
  }
  .contact__line {
    font-size: 13px;
    color: var(--text-blue);
    line-height: 1.45;
  }
  .contact__label {
    font-weight: 700;
    color: var(--brand-red);
    font-size: 11px;
  }
  .contact__line--abn {
    font-weight: 700;
    font-size: 12px;
  }
</style>
</head>
<body>
  <main class="sheet">
    <section class="card card--front" aria-label="Card front">
      <div class="brand-mark">
        <span class="brand-mark__dot"></span>
        <span class="brand-mark__initials">SVS</span>
      </div>
      <p class="brand-name">Summit Vehicle Supplies</p>
    </section>

    <section class="card card--back" aria-label="Card back">
      <div class="back-mark">
        <span class="back-mark__dot"></span>
        <span class="back-mark__initials">SVS</span>
      </div>
      <div class="contact">
        <p class="contact__name">Derek Holloway</p>
        <p class="contact__role">Director</p>
        <p class="contact__line"><span class="contact__label">M:</span> 0432 718 946</p>
        <p class="contact__line"><span class="contact__label">E:</span> info@svswebsite.com</p>
        <p class="contact__line contact__line--abn">ABN number: 71 306 548 290</p>
      </div>
    </section>
  </main>
</body>
</html>
```